deceased estate clean ups brochures

we would like a brochure to reresent our business we already have new web site and want to do DL A4 brochure to give out to promote our business we already have logo www.larkmore.com.au is where you can get all info needed

Target Market(s)

families with loved ones that have past away
people done sizing or needing to decluter

Colors
cadf82
33b8a4
886aae
33a6d7

```html
<!DOCTYPE html>
<html lang="en">
<head>
<meta charset="utf-8">
<title>Larkmore – Deceased Estate Cleanups Brochure</title>
<link href="https://fonts.googleapis.com/css2?family=Montserrat:wght@500;600;700;800&family=Open+Sans:wght@400;600;700&display=swap" rel="stylesheet">
<style>
  :root {
    --stage: #2f2f31;
    --paper: #ffffff;
    --paper-soft: #f2f2f2;
    --lime: #8dc63f;
    --lime-light: #a7d65a;
    --green-deep: #6a9f2f;
    --ink: #4a4a4a;
    --ink-soft: #6b6b6b;
    --white: #ffffff;
  }
  * { box-sizing: border-box; margin: 0; padding: 0; }
  html, body { width: 1200px; height: 800px; overflow: hidden; }
  body {
    background: var(--stage);
    font-family: "Open Sans", Arial, sans-serif;
    color: var(--ink);
    display: flex; align-items: center; justify-content: center;
  }
  .brochure {
    width: 1050px; height: 743px;
    display: grid; grid-template-columns: repeat(3, 1fr);
    box-shadow: 0 20px 50px rgba(0,0,0,.5);
  }
  .panel { position: relative; padding: 60px 44px 40px; }

  /* Inside-left panel */
  .panel--why { background: var(--paper); display: flex; flex-direction: column; }
  .why-title {
    font-family: "Montserrat", Arial, sans-serif; font-weight: 800;
    font-size: 24px; color: var(--ink); margin-bottom: 34px;
  }
  .why-title span { color: var(--lime); }
  .features { position: relative; list-style: none; }
  .features::before {
    content: ""; position: absolute; left: 17px; top: 30px; bottom: 60px;
    width: 2px; background: var(--lime-light);
  }
  .feature { position: relative; padding-left: 52px; margin-bottom: 34px; }
  .feature-icon {
    position: absolute; left: 0; top: -6px; width: 36px; height: 36px;
    border-radius: 50%; background: var(--lime); border: 3px solid #e4f1d1;
    display: flex; align-items: center; justify-content: center;
  }
  .feature-title {
    font-family: "Montserrat", Arial, sans-serif; font-weight: 700;
    font-size: 13px; color: var(--ink); margin-bottom: 10px; letter-spacing: .3px;
  }
  .feature p { font-size: 11px; line-height: 1.5; color: var(--ink-soft); }
  .call-out {
    margin-top: auto; text-align: center;
    font-family: "Montserrat", Arial, sans-serif; font-weight: 700;
    font-size: 15px; line-height: 1.35; color: var(--ink);
  }
  .web {
    text-align: center; font-size: 12px; color: var(--ink-soft); margin-top: 22px;
  }
  .web strong { color: var(--lime); font-weight: 700; }

  /* Middle panel */
  .panel--about {
    background: linear-gradient(180deg, var(--lime) 0%, var(--green-deep) 100%);
    color: var(--white); text-align: center; display: flex; flex-direction: column;
  }
  .about-title {
    font-family: "Montserrat", Arial, sans-serif; font-weight: 800;
    font-size: 20px; margin-bottom: 26px;
  }
  .panel--about p { font-size: 10.5px; line-height: 1.55; margin-bottom: 14px; opacity: .95; }
  .contact { margin-top: auto; }
  .contact-title {
    font-family: "Montserrat", Arial, sans-serif; font-weight: 800;
    font-size: 19px; line-height: 1.2; margin-bottom: 24px;
  }
  .contact-list { list-style: none; font-size: 12px; line-height: 2.1; }
  .contact-list li { display: flex; align-items: center; justify-content: center; gap: 8px; }
  .contact .web { color: var(--white); margin-top: 20px; }
  .contact .web strong { color: var(--white); }

  /* Cover panel */
  .panel--cover {
    background: linear-gradient(180deg, var(--paper-soft), var(--paper));
    display: flex; flex-direction: column; align-items: center; padding-top: 50px;
  }
  .brand { display: flex; align-items: center; gap: 12px; }
  .brand-dot { width: 22px; height: 22px; border-radius: 50%; background: var(--lime); }
  .brand-name {
    font-family: "Montserrat", Arial, sans-serif; font-weight: 700;
    font-size: 30px; letter-spacing: 3px; color: var(--ink);
  }
  .cover-photo {
    width: 280px; height: 280px; border-radius: 50%; margin-top: 38px; margin-left: 70px;
    background: radial-gradient(circle at 40% 40%, #d8ecf7 0%, #4aa6dc 45%, #2f7fc2 70%, #7cc04a 100%);
    border: 3px solid var(--paper); box-shadow: 0 0 0 2px var(--lime-light);
  }
  .badge {
    position: absolute; left: 40px; top: 370px; width: 185px; height: 185px; border-radius: 50%;
    background: linear-gradient(160deg, var(--lime-light), var(--green-deep));
    border: 6px solid rgba(255,255,255,.7);
    color: var(--white); display: flex; flex-direction: column; justify-content: center; padding-left: 30px;
  }
  .badge small { font-size: 11px; line-height: 1.3; text-transform: uppercase; }
  .badge strong {
    font-family: "Montserrat", Arial, sans-serif; font-weight: 800;
    font-size: 18px; line-height: 1.15; margin-top: 8px;
  }
  .panel--cover .web { margin-top: auto; }
</style>
</head>
<body>
<main class="brochure">

  <section class="panel panel--why">
    <h2 class="why-title">WHY <span>CHOOSE US</span></h2>
    <ul class="features">
      <li class="feature">
        <span class="feature-icon"><svg width="16" height="16" viewBox="0 0 16 16"><circle cx="8" cy="6" r="4" fill="none" stroke="#fff" stroke-width="1.6"/><path d="M5 9l-1 6 4-2 4 2-1-6" fill="none" stroke="#fff" stroke-width="1.4"/></svg></span>
        <h3 class="feature-title">QUALITY</h3>
        <p>Our goal is to enhance your property and achieve the results you are looking for. We appreciate the trust placed in us to deliver a quality job that meets your expectations.</p>
      </li>
      <li class="feature">
        <span class="feature-icon"><svg width="16" height="16" viewBox="0 0 16 16"><rect x="2" y="3" width="12" height="10" fill="none" stroke="#fff" stroke-width="1.6"/><path d="M5 6h6M5 9h6" stroke="#fff" stroke-width="1.4"/></svg></span>
        <h3 class="feature-title">PRIDE</h3>
        <p>We take pride in our family approach and care we bring to your loved ones belongings. Whether it is simple house clearing, house repairs or larger renovations your home will be ready for rental or sale.</p>
      </li>
      <li class="feature">
        <span class="feature-icon"><svg width="16" height="16" viewBox="0 0 16 16"><rect x="2" y="5" width="12" height="8" rx="1" fill="none" stroke="#fff" stroke-width="1.6"/><path d="M6 5V3h4v2" fill="none" stroke="#fff" stroke-width="1.4"/></svg></span>
        <h3 class="feature-title">PROFESSIONALISM</h3>
        <p>Larkmore only use quality staff and materials that are “fit for purpose”. We keep a professional approach to every job ensuring all agreed tasks are completed and accounted for.</p>
      </li>
    </ul>
    <p class="call-out">If you're not sure we<br>service your area, give us a call.</p>
    <p class="web">www.<strong>LarkmoreMelbourne</strong>.com.au</p>
  </section>

  <section class="panel panel--about">
    <h2 class="about-title">ABOUT US</h2>
    <p>At Larkmore our goal is to ease your worries and help you with your journey in preparing your house for rental or resale.</p>
    <p>Whether it is a move to another residence or the difficult task with dealing with the grief when a loved one passes away, Larkmore can help with the preparation of the property for sale.</p>
    <p>Larkmore will come in, remove unwanted items and dispose of all rubbish, do cosmetic repairs if required and leave the property in a spotless state.</p>
    <div class="contact">
      <h2 class="contact-title">CONTACT<br>LARKMORE TODAY!</h2>
      <ul class="contact-list">
        <li><svg width="10" height="12" viewBox="0 0 10 12"><path d="M5 11S1 6.5 1 4.5a4 4 0 018 0C9 6.5 5 11 5 11z" fill="none" stroke="#fff" stroke-width="1.3"/><circle cx="5" cy="4.5" r="1.3" fill="#fff"/></svg>PO Box 284, Seddon 3011</li>
        <li><svg width="12" height="12" viewBox="0 0 12 12"><circle cx="6" cy="6" r="5" fill="none" stroke="#fff" stroke-width="1.2"/><path d="M4 3.5l1 1.5-.7.8a4 4 0 002 2l.8-.7 1.5 1-.6 1C6 9 3 6 3 4.2z" fill="#fff"/></svg>0491 570 156</li>
        <li><svg width="13" height="10" viewBox="0 0 13 10"><rect x="1" y="1" width="11" height="8" fill="none" stroke="#fff" stroke-width="1.2"/><path d="M1 1l5.5 4.5L12 1" fill="none" stroke="#fff" stroke-width="1.2"/></svg>info@larkmoremelbourne.com.au</li>
      </ul>
      <p class="web">www.<strong>LarkmoreMelbourne</strong>.com.au</p>
    </div>
  </section>

  <section class="panel panel--cover">
    <div class="brand"><span class="brand-dot"></span><span class="brand-name">LARKMORE</span></div>
    <div class="cover-photo" role="img" aria-label="Photo of colourful cleaning spray bottles, sponges and gloves in a basket"></div>
    <div class="badge">
      <small>We're here<br>to help</small>
      <strong>DECEASED<br>ESTATE<br>CLEANUPS</strong>
    </div>
    <p class="web">www.<strong>LarkmoreMelbourne</strong>.com.au</p>
  </section>

</main>
</body>
</html>
```